Logo and label design for our product coffee scrub

We need a logo design and a packaging label design for our new brand called "Rocco Velvetine". Best design wins 500$

It's a cosmetic brand with initial product "coffee scrub", which is a body peeling made of coffee, himalayan salt and additives. Brand will target young to middle aged women, who we will address with a very sexy and slightly provocative appeal (pictures of women wearing nothing but our coffee scrub - sample attached). Purpose of the coffee scrub is to target cellulite, stretch marks, psoriasis, varicose veins, eczema and acne.

Packaging that we will use will be a brown stand up pouch (attached) with a dimensions width 13cm, height 22cm and with a front and back sticker (dimensions width 7cm, height 14cm, round corners) or sticker that overlaps from front to back.

Looking forward on receiving your ideas!

Target Market(s)

Brand will targeting young to middle aged european women, who we will address with a very sexy and slightly provocative appeal (pictures of women wearing nothing but our coffee scrub - sample attached)

Industry/Entity Type

Product

Requirements
Must have
• Just an idea for the logo writing to use a handwriting font "Rocco Velvetine".

For the front side of packaging label you could use a picture of a women's body wearing a coffee scrub. Label should be very sexy but not vulgar.
Nice to have
• The back side of the label should have a cheesy pick up line and declaration text (just a sample):

hi babe! so you wanna get dirty! just show me the way to your bath. but first let me give you a proper introduction of myself. my name is rocco and i'm a coffee scrub wearing nothing but 250g of finest arabic coffee and sweet orange flavour & lots of other good stuff.

by the way I will help you with cellulite, stretch marks, psoriasis, varicose veins, eczema and acne. i’ll smooth your lumps and bumps with brown sugar & sea salt, moisturise and tone your skin with cold pressed sweet almond oil, and use vitamins & minerals to work wonders from the outside in. then i’ll make us both smell good with a little orange essence.

ingredients:
Coffea Robusta Seed Powder (Coffee), Prunus Amygdalus Dulcis (Sweet Almond) Oil, Water (Aqua), Sodium Chloride (Salt), Sucrose (Brown Sugar). All ingredients organic.

net weight: 200 g

best before date:

barcode

```html
<!DOCTYPE html>
<html lang="en">
<head>
<meta charset="utf-8">
<title>Rocco Velvetine – Coffee Scrub Back Label</title>
<link rel="stylesheet" href="https://fonts.googleapis.com/css2?family=Italianno&family=Josefin+Sans:wght@400&display=swap">
<style>
  :root {
    --label-bg: #ffffff;
    --ink-maroon: #7a1c1c;
    --brand-brown: #8b4a2c;
    --art-light: #c08360;
    --art-dark: #7d3d24;
  }
  html, body {
    margin: 0;
    padding: 0;
    overflow: hidden;
    background: var(--label-bg);
  }
  .label {
    position: relative;
    width: 851px;
    height: 1200px;
    overflow: hidden;
    background: var(--label-bg);
    font-family: "Josefin Sans", "Gill Sans", sans-serif;
  }
  .label__artwork {
    position: absolute;
    left: 113px;
    top: 57px;
    width: 260px;
    height: 345px;
  }
  .label__brand {
    position: absolute;
    left: 350px;
    top: 28px;
    width: 270px;
    margin: 0;
    text-align: center;
    font-family: "Italianno", "Brush Script MT", cursive;
    font-weight: 400;
    font-size: 112px;
    line-height: 78px;
    color: var(--brand-brown);
  }
  .label__brand span {
    display: block;
  }
  .label__brand span + span {
    padding-left: 40px;
  }
  .label__copy {
    position: absolute;
    left: 0;
    top: 221px;
    width: 888px;
    text-align: center;
    color: var(--ink-maroon);
    font-size: 21.5px;
    line-height: 27.4px;
  }
  .label__copy p {
    margin: 0 0 27.4px;
  }
  .label__copy p:last-child {
    margin-bottom: 0;
  }
  .label__copy span {
    display: block;
  }
</style>
</head>
<body>
<main class="label">
  <svg class="label__artwork" role="img" aria-label="Illustration of two silhouetted women in coffee brown, a vintage bathtub and an ornate mirror frame" viewBox="0 0 260 345" preserveAspectRatio="none">
    <defs>
      <linearGradient id="artwork-tone" x1="0" y1="0" x2="1" y2="1">
        <stop offset="0" stop-color="var(--art-light)" stop-opacity="0.55"/>
        <stop offset="1" stop-color="var(--art-dark)" stop-opacity="0.55"/>
      </linearGradient>
    </defs>
    <path d="M0 0 H235 V150 H150 V345 H0 Z" fill="url(#artwork-tone)"/>
  </svg>

  <h1 class="label__brand"><span>Rocco</span><span>Velvetine</span></h1>

  <div class="label__copy">
    <p>
      <span>Hi babe!</span>
      <span>So you wanna get dirty!</span>
      <span>Just show me the way to your bath.</span>
      <span>but first let me give you</span>
      <span>a proper introduction of myself.</span>
      <span>My name is Rocco and i'm a</span>
      <span>coffee scrub wearing nothing</span>
      <span>but 250g of finest arabic coffee</span>
      <span>and sweet orange flavour &amp;</span>
      <span>lots of other good stuff.</span>
    </p>
    <p>
      <span>By the way I will help you with</span>
      <span>cellulite, stretch marks, psoriasis,</span>
      <span>varicose veins, eczema and acne.</span>
      <span>I’ll smooth your lumps and bumps</span>
      <span>with brown sugar &amp; sea salt,</span>
      <span>moisturise and tone your skin</span>
      <span>with cold pressed sweet almond oil,</span>
      <span>and use vitamins &amp; minerals to</span>
      <span>work wonders from the outside in.</span>
      <span>Then i’ll make us both</span>
      <span>smell good with a little orange essence.</span>
    </p>
    <p>
      <span>Ingredients:</span>
      <span>Coffea Robusta Seed Powder (Coffee),</span>
      <span>Prunus Amygdalus Dulcis (Sweet Almond) Oil,</span>
      <span>Water (Aqua), Sodium Chloride (Salt),</span>
      <span>Sucrose (Brown Sugar).</span>
      <span>All ingredients organic.</span>
    </p>
    <p><span>net weight: 200 g</span></p>
    <p><span>best before date:</span></p>
    <p><span>barcode</span></p>
  </div>
</main>
</body>
</html>
```